Packaging Design Project

PLEASE NOTE: YOU MUST USE ADOBE ILLUSTRATOR FOR THIS PROJECT.
I need a design for a plastic bag packaging for our product, Dustraline. Please see the website for more information about the product we sell, www.greenwise-home-supply.example
Colours to use are red, green and yellow of various tones and shades.
The dimensions of the bag are approximately: 20cm wide by 25cm high with a 3.5 to 4 cm side width.
Front of Bag
Must have the company logo – please see attached file A1 Q.pdf. Please separate this label in two. i.e. the company logo is only the part that says Greenwise Home Supply (with the green heartbeat design)
Also must have the product logo/signage – see the file A1 Q.pdf (attached). Please delete the Pty Ltd after the company name.
Must have product information: according to these words: “easy to use, safe around pets and children, non toxic, no chemicals”
The upper top of the bag must have the words: “resealable pack: cut here to start your cleaner, kinder future.”
The front of the bag also must have a picture relating to the product - plant and/or animal picture. Please see the website for more ideas of what pictures you can include. www.greenwise-home-supply.example. The picture must be large and take up most of the front of the bag. It must be eye catching, being the first thing the customers see.
Must have the following words somewhere on the front of the bag
• No more pests
• No more chemicals
• No more worries
• Pet friendly
Also must include: “Controls fleas, flea larvae and flea eggs: bedbugs: lice and mites: flies and biting flies: hookworm, roundworm and tapeworms”
Front must also include: KTR certification, Product of Australia, Glenhaven company logo, approximately 2 x 2 cm
Front, back and sides of bag should have the quantity amount
Sides of bag must have company name and product name
Back of bag
Must have 1 small paragraph about the company. See attached file Company Background.doc
1 small paragraph about congratulating customer for buying a clean safe effective product.- this has to be the dominant feature of the back of the bag. It must be large and eye catching
1 paragraph about Dustraline and how it works. – also included in the file Company Background.doc.
Must have an analysis of what's in the product – please see attached file
Must include rates of application – please see attached file Rates of Application.doc
Back of bag must include company logo somewhere – leave space for this
must include safety directions and barcode –please see attached file Safety Directions.doc
Updates
Forgot to tell you all that the design has to be done in Adobe Illustrator Version 10 and above. Thanks!
Reason: Hi Everyone
The project has been extended by 2 days. Keep all those designs coming in!
Hi Designers,
Here is an update to the brief which I think will make your lives easier!
Update/Changes
The dimensions of the bag are confirmed to be 21cm wide by 29cm high.
Please delete the previous information and change it to the following:
Controls fleas, bedbugs, lice, mites, flies, biting flies, hookworm, roundworm and tapeworm in pets.
Controls aphids, mealy bugs, harlequin bugs, white fly and cabbage aphids on plants.
Please put the following words under the product label, under the word "Dustraline":
Active Constituents:900g/kg amorphous silica
The safety directions has changed. It should now read:
Safety Directions
May irritate eyes and skin. Avoid contact with eyes and skin. Do not inhale dust. Wash hands after use.
Please note:
In the file we uploaded, the Dustraline label had a heartbeat line which ended with "Greenwise Home Supply....etc. Somehow everyone has lost this beepy line. Please put back the beepy line on
the Dustraline word.

```html
<!DOCTYPE html>
<html lang="en">
<head>
<meta charset="utf-8">
<title>Dustraline Bag – Front and Back</title>
<link href="https://fonts.googleapis.com/css2?family=Poppins:ital,wght@0,400;0,600;0,700;1,600&family=Yellowtail&family=Open+Sans:wght@300&display=swap" rel="stylesheet">
<style>
  :root{
    --bag-green:#1e6b35;
    --deep-green:#155a2a;
    --bright-green:#2ea84a;
    --cream:#f8f1de;
    --frame-brown:#b5804f;
    --label-grey:#6b6b6b;
    --sun-yellow:#f2c417;
    --white:#ffffff;
    --ink:#222222;
  }
  *{box-sizing:border-box;margin:0;padding:0}
  html,body{width:1200px;height:900px;overflow:hidden;background:var(--white)}
  .canvas{position:relative;width:1200px;height:900px;background:var(--white);font-family:"Poppins",sans-serif;color:var(--deep-green)}
  .abs{position:absolute}

  .bag{position:absolute;top:52px;height:780px;background:var(--bag-green)}
  .bag--front{left:20px;width:567px}
  .bag--back{left:611px;width:564px}
  .reseal-text{position:absolute;left:8px;top:8px;font-size:6.5px;letter-spacing:.2px;color:var(--white);text-transform:uppercase}
  .reseal-line{position:absolute;left:0;right:0;top:20px;border-top:1.5px dashed var(--white);opacity:.85}

  .frame{position:absolute}
  .frame path{fill:var(--cream);stroke:var(--frame-brown);stroke-width:2}

  .view-label{position:absolute;top:838px;font-family:"Open Sans",sans-serif;font-weight:300;font-size:36px;color:var(--ink)}

  .brand-name{font-weight:700;color:var(--deep-green);line-height:1.05;text-align:right}

  .illustration{position:absolute;left:158px;top:182px;width:320px;height:360px;border-radius:40% 40% 8px 8px;
    background:radial-gradient(ellipse at 50% 40%, #5f9c5a 0%, #2f7a3d 55%, rgba(47,122,61,0.15) 100%)}

  .product-label{position:absolute;left:178px;top:543px;width:250px;height:78px;border:2px dashed var(--deep-green);border-radius:10px;text-align:center}
  .product-name{font-weight:700;font-size:28px;color:var(--label-grey);letter-spacing:.5px;line-height:1;margin-top:8px}
  .product-active{font-style:italic;font-size:7.5px;color:var(--label-grey);margin-top:2px}
  .product-band{margin:2px auto 0;width:212px;background:var(--bright-green);color:var(--white);font-weight:600;font-style:italic;font-size:13px;line-height:16px;border-bottom:3px solid var(--sun-yellow)}

  .controls-head{position:absolute;left:170px;width:265px;text-align:center;font-family:"Yellowtail",cursive;font-size:34px;color:var(--deep-green);line-height:1}
  .controls-head::before,.controls-head::after{content:"";position:absolute;top:52%;width:66px;border-top:1.5px solid var(--deep-green)}
  .controls-head::before{left:0}
  .controls-head::after{right:0}
  .controls-list{position:absolute;left:130px;width:345px;text-align:center;font-weight:600;font-size:8.6px;line-height:13px;color:var(--deep-green)}

  .mini-label{position:absolute;left:680px;top:140px;width:158px;text-align:left}
  .mini-label .product-name{font-size:19px;margin-top:0}
  .mini-label .product-active{font-size:5.5px;margin-top:0}
  .mini-label .product-band{margin:1px 0 0;width:155px;font-size:9.5px;line-height:12px;border-bottom-width:2px;text-align:center}

  .section-head{position:absolute;font-family:"Yellowtail",cursive;font-size:16px;color:var(--deep-green);line-height:1}
  .centered{left:668px;width:450px;text-align:center}
  .copy{position:absolute;left:690px;width:410px;font-size:5.6px;line-height:7.2px;color:var(--deep-green)}

  .analysis{position:absolute;left:690px;top:432px;font-size:5.4px;line-height:6.7px;border-collapse:collapse;color:var(--deep-green)}
  .analysis td{padding:0}
  .analysis td:first-child{width:110px}

  .safety-box{position:absolute;left:903px;top:454px;width:180px;height:44px;border:1.5px dashed var(--deep-green);border-radius:9px;text-align:center}
  .safety-box .section-head{position:static;font-size:14px;margin-top:4px}
  .safety-box p{font-size:5.4px;line-height:7px;margin-top:4px;padding:0 8px}
</style>
</head>
<body>
<div class="canvas">

  <!-- FRONT OF BAG -->
  <section class="bag bag--front">
    <p class="reseal-text">Resealable pack: cut here to start your cleaner, kinder future.</p>
    <div class="reseal-line"></div>
  </section>

  <svg class="frame" style="left:72px;top:95px" width="465" height="710" viewBox="0 0 465 710" aria-hidden="true">
    <path d="M30,18 H190 C205,18 215,8 232,0 C249,8 259,18 274,18 H435 Q447,18 447,30 V330 C447,345 465,350 465,355 C465,360 447,365 447,380 V680 Q447,692 435,692 H274 C259,692 249,702 232,710 C215,702 205,692 190,692 H30 Q18,692 18,680 V380 C18,365 0,360 0,355 C0,350 18,345 18,330 V30 Q18,18 30,18 Z"/>
  </svg>

  <div class="abs brand-name" style="left:340px;top:134px;width:172px;font-size:17px">Greenwise<br>Home Supply</div>

  <div class="illustration" role="img" aria-label="Illustration of fruit trees with red apples, a parrot and a cat in the branches, and a cat and dog standing beneath"></div>

  <div class="product-label">
    <p class="product-name">DUSTRALINE</p>
    <p class="product-active">Active Constituents:900g/kg amorphous silica</p>
    <p class="product-band">DIATOMACEOUS EARTH</p>
  </div>

  <h2 class="controls-head" style="top:630px">Controls</h2>
  <p class="controls-list" style="top:665px">FLEAS, BEDBUGS, LICE, MITES, FLYS, BITING FLYS,<br>HOOKWORM, ROUNDWORM AND TAPEWORM IN PETS</p>
  <h2 class="controls-head" style="top:694px">Controls</h2>
  <p class="controls-list" style="top:729px">APHIDS, MEALY BUGS, HARLEQUIN BUGS, WHITE FLY<br>AND CABBAGE APHIDS ON PLANTS.</p>

  <p class="view-label" style="left:248px">FRONT</p>

  <!-- BACK OF BAG -->
  <section class="bag bag--back">
    <p class="reseal-text">Resealable pack: cut here to start your cleaner, kinder future.</p>
    <div class="reseal-line"></div>
  </section>

  <svg class="frame" style="left:662px;top:98px" width="460" height="680" viewBox="0 0 465 710" preserveAspectRatio="none" aria-hidden="true">
    <path vector-effect="non-scaling-stroke" d="M30,18 H190 C205,18 215,8 232,0 C249,8 259,18 274,18 H435 Q447,18 447,30 V330 C447,345 465,350 465,355 C465,360 447,365 447,380 V680 Q447,692 435,692 H274 C259,692 249,702 232,710 C215,702 205,692 190,692 H30 Q18,692 18,680 V380 C18,365 0,360 0,355 C0,350 18,345 18,330 V30 Q18,18 30,18 Z"/>
  </svg>

  <div class="mini-label">
    <p class="product-name">DUSTRALINE</p>
    <p class="product-active">Active Constituents:900g/kg amorphous silica</p>
    <p class="product-band">DIATOMACEOUS EARTH</p>
  </div>

  <div class="abs brand-name" style="left:930px;top:150px;width:168px;font-size:17px">Greenwise<br>Home Supply</div>

  <h3 class="section-head centered" style="top:224px">Company Background</h3>
  <p class="copy" style="top:243px">Greenwise Home Supply is an Australian company and also the first company in Australia to supply Dustraline as a means of controlling insects and pests on plants, vegetables and animals.<br>We are a company committed to finding organic ways for you to live a greener, longer, happier life, not just in the house, and but also in industry and farming.</p>

  <h3 class="section-head centered" style="top:285px">Congratulations</h3>
  <p class="copy" style="top:305px">Congratulations on your purchase of Dustraline! You have selected an exceptional product with superior performance. You should be proud of purchasing a product that is certified organic and beneficial to the environment and leaving your carbon footprint on this planet.</p>

  <h3 class="section-head centered" style="top:338px">Dustraline</h3>
  <p class="copy" style="top:357px">This is our insecticide product. A natural product registered with the National Crop and Animal Products Registry for use against insect pests of stored grain and registered as an allowable input for organic farmers by the KTR.<br>Dustra-Line kills insects by absorbing oils and waxes from the insect cuticle thus facilitating moisture loss and death by dehydration.</p>

  <h3 class="section-head" style="left:690px;top:400px;font-size:15px">Dustraline Mineral Analysis</h3>
  <p class="copy" style="top:422px">Greenwise Home Supply Dustraline contains these minerals:</p>
  <table class="analysis">
    <tr><td>Silicon Dioxide (SiO2)</td><td>90.10%</td></tr>
    <tr><td>Phosphorus Pentoxide (P2O5)</td><td>0.03%</td></tr>
    <tr><td>Aluminium Oxide (Al2O3)</td><td>4.62%</td></tr>
    <tr><td>Titanium Dioxide (TiO2)</td><td>0.37%</td></tr>
    <tr><td>Iron Oxide (Fe2O3)</td><td>3.14%</td></tr>
    <tr><td>Vanadium Oxide (V2O5)</td><td>0.03%</td></tr>
    <tr><td>Manganese Oxide (MnO)</td><td>0.02%</td></tr>
    <tr><td>Chromium Oxide (Cr2O3)</td><td>0.005%</td></tr>
    <tr><td>Magnesium Oxide (MgO)</td><td>0.54%</td></tr>
    <tr><td>Copper Oxide (CuO)</td><td>0.004%</td></tr>
    <tr><td>Calcium Oxide (CaO)</td><td>0.63%</td></tr>
    <tr><td>Zinc Oxide (ZnO)</td><td>0.007%</td></tr>
    <tr><td>Sodium Oxide (Na2O)</td><td>0.11%</td></tr>
    <tr><td>Potassium Oxide (K2O)</td><td>0.06%</td></tr>
    <tr><td>Sulphur trioxide (SO3)</td><td>0.06%</td></tr>
    <tr><td>Chlorine (Cl)</td><td>0.02%</td></tr>
  </table>

  <div class="safety-box">
    <h3 class="section-head">Safety Directions</h3>
    <p>May irritate eyes and skin. Avoid contact with eyes and skin.<br>Do not inhale dust. Wash hands after use.</p>
  </div>

  <h3 class="section-head centered" style="top:563px">Rates of Application</h3>
  <div class="copy" style="top:583px">
    <p>Poultry:</p>
    <p>0-8 weeks: use 30g Dustraline to 5kg feed, 3 times a week.<span style="position:absolute;left:218px">8-16 weeks: use 30g Dustraline per kg of feed</span></p>
    <p style="margin-top:7px">Rabbits, Guinea Pigs and Small Animals</p>
    <p>Add 1 teaspoon Dustraline per serving of grain feed. Apply monthly.</p>
    <p style="margin-top:7px">Garden:</p>
    <p>To apply Dustraline, use any dusting equipment. When spraying, apply Dustraline to upper and lower leaf surfaces to obtain the best results.</p>
    <p>When treating grain, use 80g per 1 litre of water.</p>
    <p style="margin-top:7px">Dogs and Cats</p>
    <p>When applying to dry pet foods, the following are suggested rates per kilo:</p>
    <p>•<span style="position:absolute;left:60px">Kittens: ½ teaspoon</span></p>
    <p>•<span style="position:absolute;left:60px">Cats: 1 teaspoon</span></p>
    <p>•<span style="position:absolute;left:60px">Puppies: ½ to 1 teaspoon</span></p>
    <p>•<span style="position:absolute;left:60px">Dogs under 15kg: 1 teaspoon</span></p>
    <p>•<span style="position:absolute;left:60px">Dogs over 45kg: 2 tablespoons</span></p>
    <p style="margin-top:7px">Birds</p>
    <p>Dust Dustraline between feathers of birds, repeating where necessary.</p>
    <p>Bedbugs</p>
    <p>Dust Dustraline on each leg of bed. Also, dust Dustraline onto mattress and bedding and especially on any creases of the bedding.</p>
    <p>Safety Directions</p>
    <p>Follow the label instructions which should recommend avoiding contact with</p>
  </div>

  <p class="view-label" style="left:851px">BACK</p>

</div>
</body>
</html>
```